VORTAL Business Card Design

We need a business card for a new company based on the Gold Coast, we are a new supplement distributing company called VORTAL Sports Nutrition - Bold Horizon Sports Nutrition. We are providing new science based bodybuilding and fitness supplementation. Our company has a key focus towards next generation. We are wanting a card that is cool, innovative and fresh. We would like to see the implementation of the below image in a fresh and very innovative design that stands out. The final design should communicate New, Innovative, Cool, Science and researched based.
Target Market(s)
The target market is fitness and bodybuilder enthusiasts. Young audience so very cool looking.
Industry/Entity Type
Fitness
Contact Information for Business Card
(front of card)
VORTAL Sports Nutrition.
Liam Darrow
CEO/Sport Nutrition Specialist
0472 638 904
Liam@vortalsportsfuel.example
www.vortalsportsfuel.example
(back of card)
Scientifically formulated supplement range
Private Nutrition consultations
comprehensive sports nutrition seminars
Requirements
Nice to have
- The card could have a cut out on one of the sides or one of the corners rounded off so the card looks different from a normal business card.
Should not have
- The colours need to complement each other and pop out.

```html
<!DOCTYPE html>
<html lang="en">
<head>
<meta charset="UTF-8">
<title>VORTAL Sports Nutrition – Business Card</title>
<link rel="stylesheet" href="https://fonts.googleapis.com/css2?family=Lato:wght@400;700;900&display=swap">
<style>
  :root {
    --stage: #5a5a5a;
    --card: #121314;
    --card-edge: #1c1d1f;
    --sky: #5cc6ec;
    --white: #ffffff;
    --muted: #d9d9d9;
  }
  * { box-sizing: border-box; margin: 0; padding: 0; }
  html, body {
    width: 1200px;
    height: 1000px;
    overflow: hidden;
    background: var(--stage);
    font-family: "Lato", sans-serif;
  }
  .stage {
    position: relative;
    width: 1200px;
    height: 1000px;
  }
  .card {
    position: absolute;
    left: 220px;
    width: 760px;
    height: 434px;
    background: radial-gradient(ellipse at 50% 40%, var(--card-edge), var(--card) 75%);
    overflow: hidden;
    box-shadow: 0 10px 30px rgba(0,0,0,0.35);
  }
  .card--back { top: 46px; }
  .card--front { top: 520px; border-top-right-radius: 48px; }

  /* brand lockup */
  .brand {
    display: flex;
    align-items: center;
    gap: 14px;
  }
  .brand__dot {
    width: 30px;
    height: 30px;
    border-radius: 50%;
    background: var(--sky);
  }
  .brand__name {
    font-weight: 900;
    font-size: 58px;
    letter-spacing: 3px;
    color: var(--white);
    line-height: 1;
  }
  .tagline {
    font-size: 13px;
    font-weight: 400;
    letter-spacing: 1px;
    color: var(--muted);
    text-transform: uppercase;
  }

  /* back side */
  .back__brand {
    position: absolute;
    top: 110px;
    left: 0;
    right: 0;
    display: flex;
    flex-direction: column;
    align-items: center;
    gap: 18px;
  }
  .services {
    position: absolute;
    top: 270px;
    left: 0;
    right: 0;
    list-style: none;
    display: flex;
    flex-wrap: wrap;
    justify-content: center;
    gap: 12px 34px;
    padding: 0 40px;
  }
  .services__item {
    font-size: 19px;
    color: var(--sky);
    display: flex;
    align-items: center;
    gap: 10px;
  }
  .services__item::before {
    content: "";
    width: 8px;
    height: 8px;
    border-radius: 50%;
    background: var(--white);
  }

  /* front side */
  .front__brand {
    position: absolute;
    left: 56px;
    top: 150px;
    display: flex;
    flex-direction: column;
    gap: 18px;
  }
  .front__brand .brand__name { font-size: 50px; }
  .person {
    position: absolute;
    left: 430px;
    top: 78px;
  }
  .person__name {
    font-size: 27px;
    font-weight: 700;
    color: var(--sky);
    letter-spacing: 0.5px;
  }
  .person__role {
    font-size: 16px;
    color: var(--white);
    margin-top: 2px;
  }
  .contacts {
    position: absolute;
    left: 430px;
    top: 190px;
    list-style: none;
    display: flex;
    flex-direction: column;
    gap: 14px;
  }
  .contacts__item {
    display: flex;
    align-items: center;
    gap: 12px;
    font-size: 16px;
    color: var(--white);
  }
  .contacts__icon { width: 20px; height: 18px; flex: none; }
  .band {
    position: absolute;
    height: 14px;
  }
  .band--sky { left: 0; bottom: 50px; width: 560px; background: var(--sky); }
  .band--white { right: 0; bottom: 100px; width: 180px; background: var(--white); }
</style>
</head>
<body>
<main class="stage">

  <section class="card card--back" aria-label="Card back">
    <div class="back__brand">
      <div class="brand">
        <span class="brand__dot"></span>
        <span class="brand__name">VORTAL</span>
      </div>
      <p class="tagline">Bold Horizon Sports Nutrition.</p>
    </div>
    <ul class="services">
      <li class="services__item">Scientifically Formulated Supplement Range</li>
      <li class="services__item">Private Nutrition Consultations</li>
      <li class="services__item">Comprehensive Sports Nutrition Seminars</li>
    </ul>
  </section>

  <section class="card card--front" aria-label="Card front">
    <div class="front__brand">
      <div class="brand">
        <span class="brand__dot"></span>
        <span class="brand__name">VORTAL</span>
      </div>
      <p class="tagline">Bold Horizon Sports Nutrition.</p>
    </div>

    <div class="person">
      <h1 class="person__name">LIAM DARROW</h1>
      <p class="person__role">CEO/Sport Nutrition Specialist</p>
    </div>

    <ul class="contacts">
      <li class="contacts__item">
        <svg class="contacts__icon" viewBox="0 0 20 18" aria-hidden="true">
          <path d="M2 6 Q10 0 18 6 L16 8 L13 6 L7 6 L4 8 Z" fill="var(--sky)"/>
          <rect x="4" y="9" width="12" height="8" rx="1.5" fill="var(--sky)"/>
          <circle cx="10" cy="13" r="2" fill="var(--card)"/>
        </svg>
        <span>0472 638 904</span>
      </li>
      <li class="contacts__item">
        <svg class="contacts__icon" viewBox="0 0 20 18" aria-hidden="true">
          <rect x="1" y="2" width="18" height="14" fill="var(--sky)"/>
          <path d="M1 2 L10 10 L19 2" fill="none" stroke="var(--card)" stroke-width="1.6"/>
        </svg>
        <span>Liam@vortalsportsfuel.example</span>
      </li>
      <li class="contacts__item">
        <svg class="contacts__icon" viewBox="0 0 20 18" aria-hidden="true">
          <rect x="1.5" y="1.5" width="17" height="11" fill="none" stroke="var(--sky)" stroke-width="2"/>
          <rect x="8" y="13" width="4" height="2.5" fill="var(--sky)"/>
          <rect x="5" y="15.5" width="10" height="2" fill="var(--sky)"/>
        </svg>
        <span>www.vortalsportsfuel.example</span>
      </li>
    </ul>

    <div class="band band--white"></div>
    <div class="band band--sky"></div>
  </section>

</main>
</body>
</html>
```